Visitenkarten-Design für aufstrebendes, modernes und innovatives Elektrounternehmen
Zielgruppe
Unsere Firma ist im Bereich Elektro- und Gebäudetechnik angesiedelt.
Zielgruppe sind Privatkunden und Geschäftskunden.
Wir machen alles rund um das Thema Elektrotechnik, Elektroinstallation ....
Aufgabenstellung
Es soll ein ansprechendes modernes Design sein. Gerne auch mit Rückseite.
Wir sind ein junges aufstrebendes modernes und innovatives Unternehmen

```html
<!DOCTYPE html>
<html lang="de">
<head>
<meta charset="utf-8">
<title>Veltrano – Visitenkarte</title>
<link href="https://fonts.googleapis.com/css2?family=Mulish:ital,wght@0,400;0,800;1,300&display=swap" rel="stylesheet">
<style>
  :root {
    --backdrop: #e4e4e4;
    --card: #ffffff;
    --brand-green: #bfb820;
    --brand-teal: #3b95a6;
    --ink: #1e1e1e;
    --ink-soft: #3c3c3c;
  }
  html, body {
    margin: 0;
    width: 1200px;
    height: 814px;
    overflow: hidden;
    background: var(--backdrop);
    font-family: "Mulish", sans-serif;
  }
  .sheet {
    position: relative;
    width: 1200px;
    height: 814px;
  }
  .card {
    position: absolute;
    top: 239px;
    width: 520px;
    height: 336px;
    background: var(--card);
    box-shadow: 0 10px 28px rgba(0,0,0,0.12);
    overflow: hidden;
  }
  .card--front { left: 50px; }
  .card--back { left: 630px; }

  .brand {
    position: absolute;
    left: 30px;
    top: 30px;
    display: flex;
    align-items: center;
    gap: 12px;
  }
  .brand__dot {
    width: 50px;
    height: 50px;
    border-radius: 50%;
    background: var(--brand-green);
  }
  .brand__text { display: flex; flex-direction: column; }
  .brand__name {
    font-weight: 800;
    font-size: 38px;
    line-height: 1;
    color: var(--ink-soft);
    letter-spacing: 0.5px;
  }
  .brand__tagline {
    margin-top: 3px;
    font-size: 9.5px;
    font-weight: 400;
    letter-spacing: 0.6px;
    color: var(--brand-teal);
    text-transform: uppercase;
  }

  .contact {
    position: absolute;
    right: 32px;
    top: 150px;
    text-align: right;
    color: var(--ink);
    font-size: 15px;
    line-height: 1.35;
  }
  .contact__name { margin: 0; font-weight: 400; font-size: 15px; }
  .contact__role { margin: 0 0 12px; font-style: italic; font-weight: 300; }
  .contact__lines { margin: 0 0 12px; }
  .contact__address { margin: 0; font-style: normal; }

  .back-motif {
    position: absolute;
    inset: 0;
  }
</style>
</head>
<body>
<main class="sheet">
  <section class="card card--front" aria-label="Vorderseite">
    <div class="brand">
      <span class="brand__dot" aria-hidden="true"></span>
      <div class="brand__text">
        <span class="brand__name">Veltrano</span>
        <span class="brand__tagline">Elektro- &amp; Gebäudetechnik</span>
      </div>
    </div>
    <div class="contact">
      <p class="contact__name">Jonas Veltrano</p>
      <p class="contact__role">Elektrotechnikermeister</p>
      <p class="contact__lines">T 04711 583920<br>kontakt@veltrano-elektro.de</p>
      <address class="contact__address">Lindenweg 12<br>74589 Talbrunn</address>
    </div>
  </section>

  <section class="card card--back" aria-label="Rückseite">
    <svg class="back-motif" width="520" height="336" viewBox="0 0 520 336" role="img" aria-label="Großes Markenmotiv in Grün: Stecker mit geschwungenem Kabel in einem Kreis">
      <circle cx="250" cy="30" r="290" fill="var(--brand-green)"/>
    </svg>
  </section>
</main>
</body>
</html>
```